Business Card Design

We are a contracting firm, 95% of my work is interior renovations.... but also don't want to preclude the idea of doing exterior work if it arises. I Need a business card that says I am the ultimate professional. There is a per-determined notion that all contractors are shady, unreliable, etc. Being that most of my work is in Manhattan, I would like to give the impression of fresh, modern, sleek, design/build firm.

Target Market(s)

young couples 25-40

Industry/Entity Type

Business

Contact Information for Business Card

PeterHollowayInteriors LLC
27 North Brandel Street
Marsh Hollow NY 11492
718-555-0142
646-555-0187- cell
www.phbwx.com
ph@phbwx.com
Peter Holloway

Requirements
Should not have
• do not want to give the impression of a "bargain basement store"

```html
<!DOCTYPE html>
<html lang="en">
<head>
<meta charset="utf-8">
<title>PeterHollowayInteriors – Business Card</title>
<link rel="stylesheet" href="https://fonts.googleapis.com/css2?family=Noto+Serif:wght@700&family=Open+Sans:wght@300;400;600&display=swap">
<style>
  :root {
    --page: #e6e2dc;
    --card-dark: #050505;
    --card-glow: #3a3a3a;
    --band: #262626;
    --band-edge: #9a9a9a;
    --white: #ffffff;
    --soft: #d9d9d9;
    --divider: #8a8a8a;
  }
  * { margin: 0; padding: 0; box-sizing: border-box; }
  html, body {
    width: 1200px; height: 1153px; overflow: hidden;
    background: var(--page);
  }
  .canvas { position: relative; width: 1200px; height: 1153px; }

  .card {
    position: absolute;
    width: 907px; height: 517px;
    overflow: hidden;
    color: var(--white);
    background:
      repeating-linear-gradient(90deg, rgba(255,255,255,0.018) 0 6px, rgba(0,0,0,0.03) 6px 12px),
      radial-gradient(ellipse 60% 70% at 50% 45%, var(--card-glow) 0%, #151515 55%, var(--card-dark) 100%);
    box-shadow: 0 6px 18px rgba(0,0,0,0.25);
  }
  .card--front { left: 24px; top: 44px; }
  .card--back  { left: 255px; top: 590px; }

  .company-name {
    position: absolute; left: 0; right: 0;
    text-align: center;
    font-family: "Open Sans", Arial, sans-serif;
    font-weight: 600;
    color: var(--white);
    white-space: nowrap;
  }
  .card--front .company-name { top: 106px; font-size: 44px; letter-spacing: 0.5px; }
  .tagline {
    position: absolute; left: 0; right: 0; top: 174px;
    text-align: center;
    font-family: "Open Sans", Arial, sans-serif;
    font-weight: 300; font-size: 23px;
    color: var(--soft); letter-spacing: 0.4px;
  }

  .name-band {
    position: absolute; left: 0; right: 0; top: 262px; height: 73px;
    border-top: 3px solid var(--band-edge);
    border-bottom: 3px solid var(--band-edge);
    background: #0c0c0c;
  }
  .name-band__bar {
    position: absolute; left: 0; right: 0; top: 7px; bottom: 7px;
    background: linear-gradient(180deg, #333 0%, var(--band) 50%, #1b1b1b 100%);
    border-top: 1px solid #555; border-bottom: 1px solid #111;
    display: flex; align-items: center; justify-content: center;
  }
  .person-name {
    font-family: "Noto Serif", "Times New Roman", serif;
    font-weight: 700; font-size: 29px; color: var(--white);
  }

  .contacts {
    position: absolute; left: 0; right: 0; top: 386px; height: 88px;
    font-family: "Open Sans", Arial, sans-serif;
    font-size: 22px; color: var(--white);
  }
  .contacts__divider {
    position: absolute; left: 441px; top: 0; width: 1px; height: 88px;
    background: var(--divider);
  }
  .contacts__col { position: absolute; top: 8px; display: flex; flex-direction: column; gap: 12px; }
  .contacts__col--phones { right: 483px; align-items: flex-end; }
  .contacts__col--web { left: 460px; align-items: flex-start; }
  .contact { display: flex; align-items: center; gap: 8px; height: 30px; }
  .contact svg { width: 18px; height: 18px; flex: none; }

  .card--back .company-name { top: 162px; font-size: 34px; }
  .address {
    position: absolute; left: 0; right: 0; top: 220px;
    text-align: center;
    font-family: "Open Sans", Arial, sans-serif;
    font-size: 33px; line-height: 57px; color: var(--white);
  }
  .website {
    position: absolute; left: 0; right: 0; top: 428px;
    text-align: center;
    font-family: "Open Sans", Arial, sans-serif;
    font-size: 30px; letter-spacing: 3px; color: var(--white);
  }
</style>
</head>
<body>
<div class="canvas">

  <section class="card card--front">
    <h1 class="company-name">PeterHollowayInteriors</h1>
    <p class="tagline">General Contracting &amp; Construction Services</p>

    <div class="name-band">
      <div class="name-band__bar"><span class="person-name">Peter Holloway</span></div>
    </div>

    <div class="contacts">
      <div class="contacts__col contacts__col--phones">
        <div class="contact">
          <svg viewBox="0 0 18 18" aria-hidden="true"><rect x="5" y="1" width="8" height="16" rx="1.5" fill="#fff"/><rect x="6.5" y="3" width="5" height="6" fill="#111"/><rect x="6.5" y="10.5" width="5" height="4.5" fill="#555"/></svg>
          <span>646-555-0187</span>
        </div>
        <div class="contact">
          <svg viewBox="0 0 18 18" aria-hidden="true"><circle cx="9" cy="9" r="7.5" fill="none" stroke="#fff" stroke-width="1.4"/><path d="M6 5 l2 0 l0.6 2.2 -1.2 1 a5 5 0 0 0 2.4 2.4 l1-1.2 2.2 0.6 0 2 a1 1 0 0 1 -1 1 A7 7 0 0 1 5 6 a1 1 0 0 1 1-1z" fill="#fff"/></svg>
          <span>718-555-0142</span>
        </div>
      </div>
      <div class="contacts__divider"></div>
      <div class="contacts__col contacts__col--web">
        <div class="contact">
          <svg viewBox="0 0 18 18" aria-hidden="true"><rect x="2" y="4" width="14" height="10" rx="1.5" fill="#fff"/><path d="M2.5 5 L9 10 L15.5 5" fill="none" stroke="#111" stroke-width="1.3"/></svg>
          <span>ph@phbwx.com</span>
        </div>
        <div class="contact">
          <svg viewBox="0 0 18 18" aria-hidden="true"><g fill="none" stroke="#fff" stroke-width="1.3"><circle cx="9" cy="9" r="7"/><ellipse cx="9" cy="9" rx="3" ry="7"/><path d="M2 9h14M3.5 5h11M3.5 13h11"/></g></svg>
          <span>www.phbwx.com</span>
        </div>
      </div>
    </div>
  </section>

  <section class="card card--back">
    <h2 class="company-name">PeterHollowayInteriors LLC</h2>
    <p class="address">27 North Brandel Street<br>Marsh Hollow NY 11492</p>
    <p class="website">www.phbwx.com</p>
  </section>

</div>
</body>
</html>
```